Redesign My Travel Agency Agreements

I need my reservation request forms redesigned into a professional contract. This is a travel agency contract. Just needs to look professional. PDF format please. See attached
Target Market(s)
travel agencies and travelers
Industry/Entity Type
Travel Agency
Font styles to use
Other font styles liked:
- open
Requirements
Must have
- I need my reservation request forms redesigned into a professional contract. This is a travel agency contract. Just needs to look professional. PDF format please. See attached
Nice to have
Should not have

```html
<!DOCTYPE html>
<html lang="en">
<head>
<meta charset="utf-8">
<title>Reservation Request Agreement – Page 3</title>
<link rel="stylesheet" href="https://fonts.googleapis.com/css2?family=Arimo:ital,wght@0,400;0,700;1,700&display=swap">
<style>
  :root {
    --band: #231f20;
    --ink: #231f20;
    --paper: #ffffff;
    --band-text: #ffffff;
  }
  * { margin: 0; padding: 0; box-sizing: border-box; }
  html, body {
    width: 927px; height: 1200px; overflow: hidden;
    background: var(--paper);
  }
  .page {
    position: relative; width: 927px; height: 1200px;
    font-family: "Arimo", Arial, sans-serif; color: var(--ink);
  }
  .masthead {
    position: absolute; left: 0; top: 0; width: 927px; height: 162px;
    background: var(--band); color: var(--band-text);
  }
  .brand {
    position: absolute; left: 55px; top: 66px;
    display: flex; align-items: center; gap: 12px;
    font-weight: 700; font-size: 25px; letter-spacing: 0.2px;
  }
  .brand-mark {
    width: 18px; height: 18px; background: var(--band-text);
  }
  .sender {
    position: absolute; right: 55px; top: 52px;
    text-align: right; font-weight: 700; font-size: 14.5px; line-height: 18px;
  }
  .terms {
    position: absolute; left: 55px; top: 200px; width: 818px;
    font-size: 12.6px; line-height: 16.4px;
  }
  .clause { margin-bottom: 16.4px; }
  .clause strong { font-weight: 700; }
  .fees { margin: 2px 0 14px; list-style: none; }
  .fees li { font-weight: 700; font-size: 14.8px; line-height: 22.5px; }
  .signoff {
    position: absolute; left: 55px; top: 1090px; width: 818px;
    font-weight: 700; font-size: 13px;
  }
  .field { display: flex; align-items: flex-end; margin-bottom: 18px; }
  .field-line { flex: 1; border-bottom: 1px solid var(--ink); height: 14px; margin-left: 3px; }
  .field-line.short { flex: 0 0 136px; }
  .field-line.mid { flex: 0 0 252px; margin-right: 6px; }
  .folio {
    position: absolute; right: 55px; top: 1157px;
    font-size: 9.5px; font-style: italic;
  }
  .folio strong { font-weight: 700; }
</style>
</head>
<body>
<div class="page">
  <header class="masthead">
    <div class="brand"><span class="brand-mark"></span>HARBOR LANE REWARDS</div>
    <address class="sender" style="font-style:normal">
      Harbor Lane Rewards<br>
      48 Meridian Avenue<br>
      Suite 310<br>
      Portland, OR 97204
    </address>
  </header>

  <main class="terms">
    <p class="clause"><strong>Usage Limitations:</strong> You may not use this reservation request form in conjunction with any other travel offer. Only one reservation request form per household may be used within a 12-month period. It is nontransferable and may only be used by the original recipient. This reservation request form is not intended for conventions or group travel. 7 days before and 7 days after a Major Holiday are usually not available with this offer. Offer is invalid if incomplete, illegible or altered. This reservation request form is invalid if bartered or sold to the recipient. Expired reservation request forms can be renewed for a $29 surcharge. If lost or stolen, this reservation request form can be reinstated for a $29 surcharge.</p>

    <p class="clause"><strong>Fulfillment:</strong> This reservation request form is administered and fulfilled by The Fulfillment Office. The Fulfillment Office will arrange hotel accommodations acting as an agent for hotels and/or other Travel Agencies. The Fulfillment Office will process all fees associated. The Fulfillment Office assumes no responsibility for loss, delay, accident, injury, or damage to persons, property or any liability whatsoever arising from or in conjunction with services provided. The Fulfillment Office reserves the right to substitute the components of the offered vacation and vary the itinerary should circumstances so require; destinations subject to change at any time. All federal, state and local laws apply. This offer does not include food, transportation, tips, telephone calls, or items of a personal nature. The Fulfillment Office reserves the right to offer you alternative itinerary if there is no availability during your requested travel dates. The Fulfillment Office reserves the right to book any of your date and destination combination choices. Traveler does not get to choose their cruise ship.</p>

    <p class="clause"><strong>State Disclosures:</strong> This reservation request form is not valid where restricted or prohibited by law. “This contract is for the purchase of a vacation reservation request form and puts all assignees on notice of the consumer’s right to cancel under section 559.33, Florida Statute.”</p>

    <p class="clause"><strong>Bound By Terms:</strong> By submitting all the attached reservation request form to The Fulfillment Office, the traveler consents to be bound by all the terms and provisions contained within the offer. The terms of the travel offer cannot be altered or amended except with the express written consent of an authorized officer of The Fulfillment Office.</p>

    <p class="clause"><strong>Payment For Travel Fees:</strong> We now must receive the travel fees and taxes due within 24 HOURS or your reservation request will be put on hold and you may have to start the process all over again.</p>

    <ul class="fees">
      <li>Reservation Guarantee Deposit: $50</li>
      <li>Total For All Nights Taxes &amp; Fees: $10</li>
      <li>Friday and Saturday night surcharge: $50</li>
      <li>3rd and 4th travelers surcharge: $20</li>
      <li>Grand Total: $130</li>
    </ul>

    <p class="clause">As soon as we receive the payment and apply it to your account we will send you an email to inform you that you have been put in the que to book.</p>

    <p class="clause">Keep in mind that we will contact you by email when we book a reservation for you. If you have questions please come back to the website to request help. Please note that you will need your reservation id# or certificate id# and the email you redeemed your certificate under in order to access our help system.</p>

    <p class="clause"><strong>IMPORTANT NOTE:</strong> We must receive the travel fees and taxes within 24 hours or your reservation request will be put on hold and you will have to start the reservation request process over.</p>
  </main>

  <section class="signoff">
    <div class="field">Name:<span class="field-line"></span></div>
    <div class="field">I AGREE TO THE TERMS AND CONDITIONS:<span class="field-line mid"></span>DATE/TIME STAMP:<span class="field-line short"></span></div>
  </section>

  <footer class="folio"><strong>4 Night Hotel Stay</strong> - Page 3/3</footer>
</div>
</body>
</html>
```